New Pharmaceutical Brochure Design Project

KLP Frost Carriers provides a level of service that is more than just simply transporting your pharmaceutical and healthcare products to its final destination. We fulfil your requirements by listening to your needs and provide a transport solution that totally fits your requirements.

Our mission is to provide an incomparable service for our customers that goes beyond their expectations. Our commitment to exceptional service is to demonstrate GDP, ensuring that your healthcare products are delivered with safety and arrive at their destination intact.

We invest in the highest quality temperature controlled transport equipment available, built to unique specifications, incorporating state of the art refrigeration systems, supported by audible and visual alarms and independent back up refrigeration systems. Satellite-linked position and temperature tracking technology provide our clients with a complete real-time audit trail from the point of collection to the delivery destination.

KLP Frost Carriers are continuously updating equipment and facilities, and together with a skilled and experienced workforce will continue to exceed your expectations.

KLP Frost Carriers is a specialist courier for clinical trials, transport of clinical and medical research and logistics management. It is the number one choice for Clinical Trial Project Managers, logistics consultants, and healthcare professionals, offering them solutions for time critical and temperature sensitive shipments for pre-clinical trials and phase I – IV clinical trial material.

With a thorough knowledge of clinical trial logistics, transportation regulations, compliance and documentation, as well as protocol support and packaging, KLP is uniquely qualified to meet your specific shipping needs.

We are always on call, ready to answer questions and guide you through various logistics challenges. Our logistics specialists have a unique understanding of your needs and can provide advice and solutions in-line with your project objectives.

Target Market(s)

Pharmaceutical and medical industry

Contact Information for Business Card

Ferenc Halvik, Managing Director, www.klp-frostcarriers.example, info@klp-frostcarriers.example
+44 (0) 712 5509418
+44 (0) 300 917 2264

Font styles to use
Serif
Sans Serif

Requirements
Must have
• modern vibrant images and colours in shades of blue
• all wording can be taken from our websites pharmaceutical and medical pages

```html
<!DOCTYPE html>
<html lang="en">
<head>
<meta charset="utf-8">
<title>KLP Frost Carriers – Pharmaceutical Brochure</title>
<link href="https://fonts.googleapis.com/css2?family=Montserrat:ital,wght@0,300;0,400;0,600;0,700;0,800;1,400;1,700;1,800&display=swap" rel="stylesheet">
<style>
  :root{
    --stage:#efefef;
    --paper:#f4f6f8;
    --ink:#2b2f3a;
    --navy:#1b2a8a;
    --brand:#1d4fc4;
    --brand-deep:#142f9a;
    --sky:#5aa4ea;
    --ice:#bfe1fb;
    --white:#ffffff;
  }
  *{box-sizing:border-box;margin:0;padding:0}
  html,body{width:1200px;height:900px;overflow:hidden}
  body{background:var(--stage);font-family:'Montserrat',sans-serif;color:var(--ink);position:relative}

  .spread{position:absolute;left:200px;top:167px;width:800px;height:566px;display:flex;box-shadow:0 18px 40px rgba(0,0,0,.18)}
  .panel{position:relative;width:400px;height:566px;overflow:hidden}

  /* Back panel */
  .back{background:var(--paper)}
  .back .accent-rule{position:absolute;left:48px;top:0;width:2px;height:36px;background:var(--brand)}
  .about-title{position:absolute;left:48px;top:52px;font-size:22px;font-weight:300;letter-spacing:-.5px;color:var(--ink)}
  .about-title strong{font-weight:800;font-style:italic;color:var(--navy)}
  .about-copy{position:absolute;left:48px;right:34px;top:92px;font-size:6.2px;line-height:1.55;font-style:italic;text-align:justify;color:#444}
  .back .photo{position:absolute;left:0;right:0;top:166px;height:190px;
    background:
      radial-gradient(ellipse 90px 60px at 42% 78%,#ffffff 0%,#e6f4ff 30%,rgba(150,205,245,0) 100%),
      radial-gradient(ellipse 80px 55px at 62% 30%,#f3f9ff 0%,rgba(200,230,252,.7) 40%,rgba(160,210,245,0) 100%),
      radial-gradient(ellipse 120px 90px at 22% 62%,#1a4ba8 0%,#2c6fd0 45%,rgba(70,140,220,0) 100%),
      radial-gradient(ellipse 110px 80px at 78% 68%,#3b8ae0 0%,#6fb3ee 50%,rgba(140,200,245,0) 100%),
      radial-gradient(ellipse 200px 110px at 50% 60%,#4f9be6 0%,#8fcaf4 55%,rgba(244,246,248,0) 100%);}
  .contact-band{position:absolute;left:0;right:0;bottom:0;height:220px;background:linear-gradient(160deg,var(--brand-deep) 0%,var(--brand) 60%,#1a3fb6 100%);color:var(--white)}
  .contact-band h2{position:absolute;left:72px;top:34px;font-size:7.5px;font-weight:700;font-style:italic;letter-spacing:.3px}
  .contact-list{position:absolute;left:56px;top:58px;list-style:none;font-size:7.5px;font-style:italic;font-weight:400}
  .contact-list::before{content:"";position:absolute;left:4px;top:12px;bottom:14px;width:1px;background:rgba(255,255,255,.45)}
  .contact-list li{position:relative;display:flex;gap:8px;align-items:flex-start;margin-bottom:9px;line-height:1.5}
  .contact-list svg{flex:none;margin-top:1px;background:var(--brand-deep)}
  .social-row{position:absolute;left:232px;bottom:42px;display:flex;gap:6px}
  .social-dot{width:14px;height:14px;border-radius:50%;border:1px solid rgba(255,255,255,.85);background:rgba(255,255,255,.12)}

  /* Front cover */
  .cover{background:linear-gradient(180deg,#a9d4f6 0%,#5fa6ea 38%,#2f74d8 70%,#2459cf 100%)}
  .cover .photo{position:absolute;left:0;top:0;width:400px;height:420px;
    background:
      radial-gradient(ellipse 100px 90px at 74% 64%,#ffffff 0%,#eef3f8 40%,rgba(220,232,245,0) 100%),
      radial-gradient(ellipse 60px 40px at 70% 50%,#dfe9f4 0%,rgba(200,220,240,0) 100%),
      radial-gradient(ellipse 140px 90px at 62% 16%,#d8ebfb 0%,rgba(150,200,245,.6) 45%,rgba(120,180,240,0) 100%),
      radial-gradient(circle 10px at 50% 8%,#e36a86 0%,rgba(227,106,134,0) 100%),
      radial-gradient(circle 10px at 70% 12%,#d9526f 0%,rgba(217,82,111,0) 100%),
      radial-gradient(circle 10px at 58% 20%,#3f6fd6 0%,rgba(63,111,214,0) 100%),
      radial-gradient(ellipse 150px 110px at 24% 72%,#2d6fd3 0%,#5ea6ea 50%,rgba(95,166,234,0) 100%),
      linear-gradient(180deg,#b7dcf8 0%,#78b8ef 45%,rgba(47,116,216,0) 100%);}
  .cover .band{position:absolute;left:0;right:0;top:400px;bottom:0;background:linear-gradient(170deg,#2e6fd6 0%,#2459cf 100%)}
  .logo-badge{position:absolute;right:14px;top:96px;width:112px;height:112px;border-radius:50%;background:var(--white);display:flex;align-items:center;justify-content:center;text-align:center;box-shadow:0 0 0 5px rgba(255,255,255,.35)}
  .logo-badge span{font-size:11px;font-weight:700;color:var(--navy);line-height:1.2}
  .title-rule{position:absolute;left:40px;top:392px;width:150px;height:3px;background:var(--white)}
  .cover-title{position:absolute;left:40px;top:404px;font-size:24px;font-weight:800;line-height:1.05;color:var(--white);letter-spacing:.3px}
  .cover-sub{position:absolute;left:40px;top:464px;width:260px;font-size:8.5px;font-weight:300;line-height:1.45;letter-spacing:.6px;text-transform:uppercase;color:#dbe9ff}
  .cover-url{position:absolute;right:26px;bottom:30px;writing-mode:vertical-rl;transform:rotate(180deg);font-size:8px;color:var(--white);letter-spacing:.4px}
  .url-rule{position:absolute;right:14px;bottom:30px;width:1px;height:70px;background:rgba(255,255,255,.8)}
</style>
</head>
<body>
<main class="spread">
  <section class="panel back">
    <div class="accent-rule"></div>
    <h1 class="about-title">ABOUT <strong>US</strong></h1>
    <p class="about-copy">Experience speaks for itself and here at KLP Frost Carriers we have many years experience in the haulage industry and in particular Temperature Controlled Transportation. As a CPC holder experienced in costing, time and route planning, sub contracting and logistics management we ensure your delivery or collection is on time, tracked and audited, leaving you to get on with running your business. Our fully employed drivers are smart and professional and have a mass of industry knowledge and experience. When your goods are transported by KLP you can be assured that our drivers will be great ambassadors for your business. KLP Frost Carriers are full members of the NHG, which is a mark of our standing in the industry.</p>
    <div class="photo" role="img" aria-label="Global logistics montage with aircraft, cargo ship, containers and lorries in blue tones"></div>
    <div class="contact-band">
      <h2>KLP FROST CARRIERS</h2>
      <ul class="contact-list">
        <li><svg width="8" height="10" viewBox="0 0 8 10"><path d="M4 0a3.5 3.5 0 0 1 3.5 3.5C7.5 6 4 10 4 10S.5 6 .5 3.5A3.5 3.5 0 0 1 4 0z" fill="none" stroke="#fff" stroke-width="1"/><circle cx="4" cy="3.5" r="1.1" fill="#fff"/></svg><span>Unit 7, Larkfield Trade Park,<br>Millbrook Road, Harwell, HW4 2QT</span></li>
        <li><svg width="9" height="9" viewBox="0 0 10 10"><path d="M2 1l2 2-1 1.2c.6 1.3 1.5 2.2 2.8 2.8L7 6l2 2-1.4 1.5C4 9 1 6 .5 2.4z" fill="none" stroke="#fff" stroke-width="1"/></svg><span>+44 (0) 300 917 2264</span></li>
        <li><svg width="9" height="8" viewBox="0 0 10 8"><rect x=".5" y=".5" width="9" height="7" fill="none" stroke="#fff"/><path d="M.5 .5L5 4.5 9.5.5" fill="none" stroke="#fff"/></svg><span>info@klp-frostcarriers.example</span></li>
        <li><svg width="9" height="9" viewBox="0 0 10 10"><circle cx="5" cy="5" r="4.5" fill="none" stroke="#fff"/><path d="M.5 5h9M5 .5c2.5 2.5 2.5 6.5 0 9M5 .5c-2.5 2.5-2.5 6.5 0 9" fill="none" stroke="#fff" stroke-width=".8"/></svg><span>www.klp-frostcarriers.example</span></li>
      </ul>
      <div class="social-row" aria-label="Social media links">
        <span class="social-dot"></span><span class="social-dot"></span><span class="social-dot"></span>
      </div>
    </div>
  </section>

  <section class="panel cover">
    <div class="band"></div>
    <div class="photo" role="img" aria-label="White refrigerated lorry in front of a glowing world map, with laboratory glassware and molecule models above, in blue tones"></div>
    <div class="logo-badge"><span>KLP Frost<br>Carriers</span></div>
    <div class="title-rule"></div>
    <h1 class="cover-title">PHARMACEUTICAL<br>TRANSPORT SERVICES</h1>
    <p class="cover-sub">KLP Frost Carriers provides same day and next day pharmaceutical logistics services across the UK &amp; Europe</p>
    <div class="url-rule"></div>
    <p class="cover-url">www.klp-frostcarriers.example</p>
  </section>
</main>
</body>
</html>
```